Brightwell Electrical and Air conditioning services needs Designer Van Signage.

Brightwell Electrical and Air conditioning company needs a Van signage designed to give customers a professional image of the business. Attached are some sample design that we will be interested in. Do not need full van wrap, Back Half should be ok.

Industry/Entity Type

Electrical, Air conditioning, & Plumbing

Requirements
Must have
• 24 hour emergency service. Electrical , Air conditioning & Plumbing ideas. Please show all around van. front back and 2 sides.
Nice to have
• Please use mobile number: 0437205816, email: info@brightwellelectrical-example.com.au, Web: www.brightwellelectrical-example.com.au.
Should not have
• Full van wrap

```html
<!DOCTYPE html>
<html lang="en">
<head>
<meta charset="utf-8">
<title>Brightwell Van Signage</title>
<link rel="stylesheet" href="https://fonts.googleapis.com/css2?family=Montserrat:ital,wght@0,600;0,700;0,800;1,800&display=swap">
<style>
  :root {
    --orange: #e8862a;
    --blue: #1f56a8;
    --navy: #1b3f86;
    --red: #d9262c;
    --green: #2aa83a;
    --yellow: #f2c21a;
    --white: #ffffff;
    --ground: #e6e7ea;
    --divider: #cfd2d8;
  }
  * { margin: 0; padding: 0; box-sizing: border-box; }
  html, body { width: 1200px; height: 2700px; overflow: hidden; }
  body {
    background: var(--ground);
    font-family: "Montserrat", Arial, sans-serif;
  }
  .view {
    position: relative;
    width: 1200px;
    height: 900px;
    display: flex;
    align-items: center;
    justify-content: center;
    border-bottom: 2px solid var(--divider);
  }
  .view:last-child { border-bottom: none; }
  .panel { display: block; filter: drop-shadow(0 6px 14px rgba(0,0,0,.12)); }
  .brand-name { font-weight: 800; fill: var(--orange); }
  .tag { font-weight: 700; }
  .tag-electrical { fill: var(--red); }
  .tag-air { fill: var(--blue); }
  .tag-plumbing { fill: var(--orange); }
  .pill-text { font-weight: 700; fill: var(--white); letter-spacing: .5px; }
  .phone-text { font-weight: 800; fill: var(--white); }
  .web-text { font-weight: 700; }
  .small-text { font-weight: 600; }
</style>
</head>
<body>

<!-- Side livery -->
<section class="view view-side">
  <svg class="panel" width="1120" height="440" viewBox="0 0 1120 440">
    <defs>
      <linearGradient id="phoneGradSide" x1="0" x2="1">
        <stop offset="0" stop-color="#f2d21a"/>
        <stop offset=".55" stop-color="#f08a1c"/>
        <stop offset="1" stop-color="#d9262c"/>
      </linearGradient>
    </defs>
    <rect class="side-base" x="0" y="0" width="1120" height="440" rx="26" fill="var(--white)"/>
    <polygon class="side-orange-band" points="0,150 550,214 430,310 1120,372 1120,394 400,338 510,246 0,192" fill="var(--orange)"/>
    <polygon class="side-blue-band" points="0,210 520,258 400,352 1120,400 1120,440 0,440" fill="var(--blue)"/>

    <g class="side-brand">
      <circle cx="90" cy="78" r="46" fill="var(--orange)"/>
      <text class="brand-name" x="160" y="104" font-size="80">Brightwell</text>
      <text class="tag" x="162" y="140" font-size="21">
        <tspan class="tag-electrical">Electrical</tspan>
        <tspan class="tag-air" dx="10">Air Conditioning</tspan>
        <tspan class="tag-plumbing" dx="10">Plumbing</tspan>
      </text>
    </g>

    <g class="side-phone">
      <rect x="250" y="158" width="260" height="40" rx="8" fill="url(#phoneGradSide)"/>
      <circle cx="262" cy="178" r="18" fill="var(--white)" stroke="var(--blue)" stroke-width="3"/>
      <path d="M255 170 q2 -3 5 0 l2 4 q-2 3 0 5 q2 3 5 4 q2 -2 5 0 l3 3 q0 3 -4 4 q-9 0 -16 -10 q-3 -6 0 -10z" fill="var(--blue)"/>
      <text class="phone-text" x="290" y="190" font-size="28">1300 552 419</text>
    </g>

    <text class="web-text side-web" x="30" y="240" font-size="18" textLength="438" lengthAdjust="spacingAndGlyphs" transform="rotate(5.27 30 212)" fill="var(--white)">www.<tspan fill="var(--orange)">brightwell</tspan>electrical-example.com.au</text>

    <g class="side-emergency">
      <text x="700" y="190" font-size="50" font-weight="800" font-style="italic" fill="var(--blue)">24/7</text>
      <text x="830" y="170" font-size="20" font-weight="800" fill="var(--navy)">Emergency</text>
      <rect x="830" y="176" width="84" height="20" rx="3" fill="var(--red)"/>
      <text x="836" y="191" font-size="13" font-weight="800" fill="var(--white)">SERVICES</text>
    </g>

    <g class="side-services">
      <rect x="560" y="222" width="160" height="28" rx="14" fill="var(--red)"/>
      <circle cx="574" cy="236" r="12" fill="var(--white)"/>
      <text class="pill-text" x="592" y="242" font-size="15">ELECTRICAL</text>

      <rect x="730" y="222" width="140" height="28" rx="14" fill="var(--red)"/>
      <circle cx="744" cy="236" r="12" fill="var(--orange)"/>
      <text class="pill-text" x="762" y="242" font-size="15">PLUMBING</text>

      <rect x="520" y="260" width="200" height="28" rx="14" fill="var(--blue)"/>
      <circle cx="534" cy="274" r="12" fill="var(--white)"/>
      <text class="pill-text" x="552" y="280" font-size="15">AIR CONDITIONING</text>

      <rect x="730" y="260" width="170" height="28" rx="14" fill="var(--green)"/>
      <circle cx="744" cy="274" r="12" fill="var(--white)"/>
      <text class="pill-text" x="762" y="280" font-size="15">CCTV SECURITY</text>
    </g>

    <text class="small-text" x="540" y="306" font-size="15" fill="var(--navy)">Installation, Service, Repairs and Maintenance.</text>
    <text class="small-text" x="360" y="410" font-size="14" fill="var(--white)">Electrical License Number - PGE204817</text>
  </svg>
</section>

<!-- Rear livery -->
<section class="view view-rear">
  <svg class="panel" width="760" height="640" viewBox="0 0 760 640">
    <defs>
      <linearGradient id="phoneGradRear" x1="0" x2="1">
        <stop offset="0" stop-color="#f2d21a"/>
        <stop offset=".55" stop-color="#f08a1c"/>
        <stop offset="1" stop-color="#d9262c"/>
      </linearGradient>
    </defs>
    <rect x="0" y="0" width="760" height="640" rx="24" fill="var(--white)"/>
    <rect class="rear-orange-top" x="0" y="222" width="760" height="20" fill="var(--orange)"/>
    <rect class="rear-orange-main" x="0" y="250" width="760" height="38" fill="var(--orange)"/>
    <rect class="rear-blue" x="0" y="296" width="760" height="344" fill="var(--blue)"/>
    <rect x="0" y="382" width="760" height="6" fill="var(--white)"/>
    <rect x="0" y="430" width="760" height="4" fill="var(--white)"/>

    <g class="rear-brand">
      <circle cx="110" cy="125" r="70" fill="var(--orange)"/>
      <text class="brand-name" x="218" y="150" font-size="84">Brightwell</text>
      <text class="tag" x="222" y="190" font-size="21">
        <tspan class="tag-electrical">Electrical</tspan>
        <tspan class="tag-air" dx="10">Air Conditioning</tspan>
        <tspan class="tag-plumbing" dx="10">Plumbing</tspan>
      </text>
    </g>

    <g class="rear-services">
      <rect x="14" y="392" width="730" height="30" fill="var(--green)"/>
      <rect x="14" y="392" width="170" height="30" fill="var(--red)"/>
      <rect x="184" y="392" width="150" height="30" fill="var(--red)"/>
      <rect x="334" y="392" width="210" height="30" fill="var(--blue)"/>
      <circle cx="30" cy="407" r="12" fill="var(--white)"/>
      <text class="pill-text" x="48" y="413" font-size="15">ELECTRICAL</text>
      <circle cx="198" cy="407" r="12" fill="var(--orange)"/>
      <text class="pill-text" x="216" y="413" font-size="15">PLUMBING</text>
      <circle cx="348" cy="407" r="12" fill="var(--white)"/>
      <text class="pill-text" x="366" y="413" font-size="15">AIR CONDITIONING</text>
      <circle cx="560" cy="407" r="12" fill="var(--white)"/>
      <text class="pill-text" x="580" y="413" font-size="15">CCTV SECURITY</text>
    </g>

    <text class="small-text" x="380" y="462" font-size="17" fill="var(--white)" text-anchor="middle">Installation, Service, Repairs and Maintenance.</text>

    <g class="rear-phone">
      <rect x="170" y="486" width="430" height="56" rx="10" fill="url(#phoneGradRear)"/>
      <circle cx="190" cy="514" r="28" fill="var(--white)" stroke="var(--blue)" stroke-width="3"/>
      <path d="M180 502 q3 -4 7 0 l3 6 q-3 4 0 7 q3 4 7 6 q3 -3 7 0 l4 4 q0 4 -6 6 q-13 0 -23 -15 q-4 -9 1 -14z" fill="var(--blue)"/>
      <text class="phone-text" x="232" y="530" font-size="42">1300 552 419</text>
    </g>

    <text class="web-text" x="380" y="604" font-size="22" fill="var(--white)" text-anchor="middle">www.<tspan fill="var(--orange)">brightwell</tspan>electrical-example.com.au</text>
  </svg>
</section>

<!-- Front bonnet -->
<section class="view view-front">
  <svg class="panel" width="820" height="260" viewBox="0 0 820 260">
    <rect x="0" y="0" width="820" height="260" rx="24" fill="var(--white)"/>
    <g class="front-brand">
      <circle cx="150" cy="125" r="78" fill="var(--orange)"/>
      <text class="brand-name" x="260" y="145" font-size="82">Brightwell</text>
      <text class="tag" x="264" y="184" font-size="20">
        <tspan class="tag-electrical">Electrical</tspan>
        <tspan class="tag-air" dx="10">Air Conditioning</tspan>
        <tspan class="tag-plumbing" dx="10">Plumbing</tspan>
      </text>
    </g>
  </svg>
</section>

</body>
</html>
```